plumbers buisness card

A buisness card for a plumbing buisness
needs to have a water theme with navy blue, light blue and white
with an image of either a water drop, pipes, tools or something relating to plumbing and incorperating my buisness name as a logo

"Talcott Plumbing" is the words that need to stand out with "& gasfitting" to be smaller
Updates

spelling error on brief, "maintenance"
and also could you include my email m_talcott@nimbrel.com.au

Industry/Entity Type

Plumbing

Contact Information for Business Card

Talcott Plumbing & Gasfitting

myles talcott
0492315806

specialising in
-new homes
-maitenance
-renovations

license no.
-73846

```html
<!DOCTYPE html>
<html lang="en">
<head>
<meta charset="utf-8">
<title>Talcott Plumbing &amp; Gasfitting – Business Card</title>
<link rel="stylesheet" href="https://fonts.googleapis.com/css2?family=Tinos&display=swap">
<style>
  :root{
    --stage:#000000;
    --card-white:#ffffff;
    --card-blue:#6c9ac6;
    --card-blue-deep:#5f8dbb;
    --ring-blue:#9dbde3;
    --brand-red:#e8232a;
    --line-black:#0b0b0b;
    --text-light:#d3e1f1;
    --back-light:#f2f2f2;
    --back-grey:#b3b3b3;
  }
  *{margin:0;padding:0;box-sizing:border-box}
  html,body{width:1200px;height:1000px;overflow:hidden;background:var(--stage)}
  body{position:relative;font-family:"Tinos","Times New Roman",serif}

  .card{position:absolute;width:760px;height:420px;border-radius:34px;overflow:hidden}
  .card--front{left:70px;top:50px;background:var(--card-white)}
  .card--back{left:370px;top:530px;
    background:radial-gradient(ellipse at 48% 45%,var(--back-light) 0%,#d6d6d6 40%,var(--back-grey) 100%)}

  .front-bands{position:absolute;inset:0;width:100%;height:100%}

  .brand-ring{position:absolute;left:62px;top:150px;width:104px;height:104px;
    border:8px solid var(--ring-blue);border-radius:50%;background:var(--card-white)}

  .brand-name{position:absolute;left:190px;top:46px;color:var(--brand-red);
    font-size:56px;font-weight:400;line-height:1;white-space:nowrap}
  .brand-sub{position:absolute;left:300px;top:108px;color:var(--brand-red);
    font-size:34px;line-height:1;white-space:nowrap}

  .contact{position:absolute;right:56px;top:196px;text-align:right;color:var(--text-light)}
  .contact__name{font-size:44px;line-height:1;margin-bottom:14px}
  .contact__line{font-size:22px;line-height:1.45;display:flex;justify-content:flex-end;align-items:center;gap:10px}
  .contact__icon{width:18px;height:18px;flex:none}

  .services{position:absolute;left:46px;top:262px;color:var(--text-light)}
  .services__title{font-size:34px;line-height:1;margin-bottom:8px}
  .services__list{list-style:none;padding-left:28px;font-size:22px;line-height:1.12}

  .back-mark{position:absolute;left:50%;top:50%;transform:translate(-50%,-50%);
    display:flex;flex-direction:column;align-items:center;gap:18px}
  .back-mark__ring{width:190px;height:190px;border:12px solid var(--ring-blue);
    border-radius:50%;background:var(--card-white)}
  .back-mark__name{color:var(--card-blue-deep);font-size:34px;white-space:nowrap}
</style>
</head>
<body>

<section class="card card--front" aria-label="Business card front">
  <svg class="front-bands" viewBox="0 0 760 420" preserveAspectRatio="none" aria-hidden="true">
    <path d="M0 262 Q 400 262 760 92 L760 420 L0 420 Z" fill="var(--card-blue)"/>
    <path d="M0 248 Q 400 248 760 78" fill="none" stroke="var(--line-black)" stroke-width="6"/>
    <path d="M0 256 Q 400 256 760 86" fill="none" stroke="var(--brand-red)" stroke-width="6"/>
  </svg>

  <div class="brand-ring" aria-hidden="true"></div>
  <h1 class="brand-name">Talcott Plumbing</h1>
  <p class="brand-sub">&amp; gasfitting</p>

  <div class="contact">
    <p class="contact__name">myles talcott</p>
    <p class="contact__line">0492315806
      <svg class="contact__icon" viewBox="0 0 24 24" aria-hidden="true"><path d="M6.6 10.8a15 15 0 0 0 6.6 6.6l2.2-2.2c.3-.3.7-.4 1-.2 1.1.4 2.3.6 3.6.6.6 0 1 .4 1 1V20c0 .6-.4 1-1 1A17 17 0 0 1 3 4c0-.6.4-1 1-1h3.5c.6 0 1 .4 1 1 0 1.2.2 2.4.6 3.6.1.3 0 .7-.2 1z" fill="var(--card-white)"/></svg>
    </p>
    <p class="contact__line">m_talcott@nimbrel.com.au
      <svg class="contact__icon" viewBox="0 0 24 24" aria-hidden="true"><rect x="2.5" y="5.5" width="19" height="13" fill="none" stroke="var(--card-white)" stroke-width="1.6"/><path d="M2.5 5.5 12 13l9.5-7.5" fill="none" stroke="var(--card-white)" stroke-width="1.6"/></svg>
    </p>
  </div>

  <div class="services">
    <p class="services__title">Specialising in :-</p>
    <ul class="services__list">
      <li>New Homes</li>
      <li>Maintenance</li>
      <li>Renovation</li>
      <li>License No -73846</li>
    </ul>
  </div>
</section>

<section class="card card--back" aria-label="Business card back">
  <div class="back-mark">
    <div class="back-mark__ring" aria-hidden="true"></div>
    <p class="back-mark__name">Talcott Plumbing</p>
  </div>
</section>

</body>
</html>
```